Business card design needed for Automotive Reconditioning business

I have a logo design i just cant decide on the best color or layout for the business card, I will upload all the files so you can see all colors schemes we are considering. I have other file formats if needed let me know.

Target Market(s)

automotive dealerships

Contact Information for Business Card

HERE are the Descriptions and info needed on the card:
Interior Repair: Leather carpet burns panels dash Deoderize
Dealer products and Vin Verify
( spot for name and cell number) My name is Norman Bexley phone 614 352-4180 Title COO www.QuorvalMotive.com

Font styles to use
Sans Serif
Other font styles liked:
• what ever you think looks best

Requirements
Must have
• Must be able to change the name and phone for employees

```html
<!DOCTYPE html>
<html lang="en">
<head>
<meta charset="utf-8">
<title>Quorval Motive – Business Card</title>
<link rel="stylesheet" href="https://fonts.googleapis.com/css2?family=Exo+2:wght@400;600;700&display=swap">
<style>
  :root {
    --bg: #e9e6e1;
    --card-dark: #262626;
    --card-light: #ffffff;
    --brand-blue: #1f6fc0;
    --brand-red: #e5322b;
    --ink: #2b2b2b;
    --rule: #8a8a8a;
  }
  * { box-sizing: border-box; margin: 0; padding: 0; }
  html, body { width: 1200px; height: 1021px; overflow: hidden; }
  body {
    background: var(--bg);
    font-family: "Exo 2", sans-serif;
    position: relative;
  }
  .card {
    position: absolute;
    width: 660px;
    height: 377px;
    box-shadow: 0 10px 30px rgba(0,0,0,0.18);
  }
  .card--front { left: 380px; top: 80px; background: var(--card-dark); }
  .card--back { left: 170px; top: 520px; background: var(--card-light); }

  .brand {
    display: flex;
    align-items: center;
    gap: 12px;
    color: var(--brand-blue);
    font-weight: 700;
  }
  .brand__mark { width: 16px; height: 16px; background: var(--brand-red); flex: none; }
  .brand__name { text-transform: uppercase; }
  .brand__name span { display: block; }
  .brand__title { line-height: 1.3; }
  .brand__sub { line-height: 1.2; }

  .card--front .brand {
    position: absolute; left: 0; right: 0; top: 50%;
    transform: translateY(-50%);
    justify-content: center;
  }
  .card--front .brand__name .brand__title { font-size: 46px; letter-spacing: 1px; }
  .card--front .brand__name .brand__sub { font-size: 17px; letter-spacing: 2px; margin-top: 6px; }
  .card--front .brand__mark { width: 22px; height: 22px; }

  .card--back .brand { position: absolute; left: 40px; top: 104px; }
  .card--back .brand__name .brand__title { font-size: 30px; }
  .card--back .brand__name .brand__sub { font-size: 11px; letter-spacing: 1px; margin-top: 4px; }

  .divider {
    position: absolute; left: 330px; top: 100px;
    width: 1px; height: 110px; background: var(--rule);
  }
  .contact { position: absolute; left: 356px; top: 104px; color: var(--ink); }
  .contact__name {
    color: var(--brand-blue); font-weight: 700; font-size: 26px;
    text-transform: uppercase; line-height: 1.1;
  }
  .contact__title { font-size: 17px; margin-top: 2px; }
  .contact__line {
    display: flex; align-items: center; gap: 8px;
    font-size: 17px; margin-top: 6px;
  }
  .contact__line svg { width: 16px; height: 16px; flex: none; }
  .contact__line:first-of-type { margin-top: 12px; }

  .services {
    position: absolute; left: 40px; right: 40px; top: 262px;
    font-size: 17px; line-height: 1.4; color: var(--ink); text-align: center;
  }
  .services__label { color: var(--brand-red); }
</style>
</head>
<body>
  <section class="card card--front" aria-label="Card front">
    <div class="brand">
      <div class="brand__mark"></div>
      <div class="brand__name">
        <span class="brand__title">Quorval Motive</span>
        <span class="brand__sub">Auto Reconditioning Corp.</span>
      </div>
    </div>
  </section>

  <section class="card card--back" aria-label="Card back">
    <div class="brand">
      <div class="brand__mark"></div>
      <div class="brand__name">
        <span class="brand__title">Quorval Motive</span>
        <span class="brand__sub">Auto Reconditioning Corp.</span>
      </div>
    </div>

    <div class="divider"></div>

    <div class="contact">
      <p class="contact__name">Norman Bexley</p>
      <p class="contact__title">COO</p>
      <p class="contact__line">
        <svg viewBox="0 0 16 16" aria-hidden="true"><rect x="4" y="1" width="8" height="14" rx="1.5" fill="none" stroke="var(--brand-red)" stroke-width="1.4"/><line x1="7" y1="12.5" x2="9" y2="12.5" stroke="var(--brand-red)" stroke-width="1.4"/></svg>
        614 352-4180
      </p>
      <p class="contact__line">
        <svg viewBox="0 0 16 16" aria-hidden="true"><g fill="none" stroke="var(--brand-red)" stroke-width="1.2"><circle cx="8" cy="8" r="6.5"/><ellipse cx="8" cy="8" rx="3" ry="6.5"/><line x1="1.5" y1="8" x2="14.5" y2="8"/><line x1="2.5" y1="4.8" x2="13.5" y2="4.8"/><line x1="2.5" y1="11.2" x2="13.5" y2="11.2"/></g></svg>
        www.QuorvalMotive.com
      </p>
    </div>

    <p class="services">
      <span class="services__label">Interior Repair:</span> Leather carpet burns panels dash Deoderize<br>
      Dealer products and Vin Verify
    </p>
  </section>
</body>
</html>
```